Apricot Variety Sheet - Meadowlark Orchard Co

We are needing a variety sheet that we can hand out that will describe the different apricot vatieties we have available. The attached document has the name of the variety along with a description that will need to be on the sheet. We are looking for a modern, appealing way to display this information on 1 page (if needed, it can be front and back)
Updates

Apologies for the delay; we are overwhelmed with the great design options and will be sorting through them all (across our contests) to pick a collective. Thank you for your patience.

Target Market(s)

Growers and consumers

Industry/Entity Type

Agriculture

Requirements
Must have
• Easy to read
• Natural color palettes to emphasize the agricultural nature
• Clearly show washington as the origin in the title or at the top
Nice to have
• incorporate Apricots in the design

```html
<!DOCTYPE html>
<html lang="en">
<head>
<meta charset="UTF-8">
<title>Apricot Variety Sheet – Meadowlark Orchard Co</title>
<link href="https://fonts.googleapis.com/css2?family=Montserrat:wght@400;600;700&family=Open+Sans:wght@400&display=swap" rel="stylesheet">
<style>
  :root {
    --backdrop: #f1e6d6;
    --coral: #f36f6c;
    --forest: #1c6b43;
    --ink: #2b2b2b;
    --paper: #ffffff;
    --apricot-light: #fbc45a;
    --apricot-mid: #f3a23e;
    --apricot-deep: #e0772c;
  }
  * { box-sizing: border-box; margin: 0; padding: 0; }
  html, body {
    width: 1200px;
    height: 1200px;
    overflow: hidden;
    background: var(--backdrop);
  }
  .sheet {
    position: absolute;
    left: 152px;
    top: 20px;
    width: 896px;
    height: 1160px;
  }
  .sheet-photo {
    position: absolute;
    inset: 0;
    background:
      radial-gradient(circle at 15% 10%, var(--apricot-light) 0 12%, transparent 30%),
      radial-gradient(circle at 85% 30%, var(--apricot-light) 0 10%, transparent 28%),
      radial-gradient(circle at 10% 70%, var(--apricot-deep) 0 8%, transparent 26%),
      radial-gradient(circle at 90% 85%, var(--apricot-light) 0 10%, transparent 30%),
      linear-gradient(160deg, var(--apricot-mid), var(--apricot-deep) 55%, var(--apricot-mid));
  }
  .sheet-panel {
    position: absolute;
    left: 42px;
    right: 42px;
    top: 42px;
    bottom: 42px;
    background: var(--paper);
    padding: 36px 42px 0;
    display: flex;
    flex-direction: column;
    align-items: center;
  }
  .sheet-title {
    display: flex;
    align-items: center;
    width: 100%;
    gap: 30px;
    font-family: "Montserrat", sans-serif;
    font-weight: 400;
    font-size: 36px;
    letter-spacing: 0.5px;
    color: var(--coral);
    line-height: 40px;
    white-space: nowrap;
  }
  .sheet-title::before,
  .sheet-title::after {
    content: "";
    flex: 1;
    height: 3px;
    background: var(--coral);
  }
  .sheet-origin {
    margin-top: 6px;
    font-family: "Montserrat", sans-serif;
    font-weight: 600;
    font-size: 14px;
    line-height: 18px;
    letter-spacing: 3px;
    color: var(--forest);
  }
  .variety-list {
    list-style: none;
    margin-top: 14px;
    width: 100%;
    display: flex;
    flex-direction: column;
    gap: 16px;
  }
  .variety {
    text-align: center;
  }
  .variety-name {
    font-family: "Montserrat", sans-serif;
    font-weight: 700;
    font-size: 20px;
    line-height: 22px;
    letter-spacing: 0.5px;
    color: var(--forest);
  }
  .variety-text {
    font-family: "Open Sans", sans-serif;
    font-size: 14.5px;
    line-height: 16.5px;
    color: var(--ink);
    white-space: nowrap;
  }
  .sheet-footer {
    margin-top: auto;
    margin-bottom: 42px;
    width: 100%;
    height: 42px;
    background: var(--forest);
    color: var(--paper);
    font-family: "Montserrat", sans-serif;
    font-weight: 700;
    font-size: 19px;
    display: flex;
    align-items: center;
    justify-content: center;
  }
</style>
</head>
<body>
  <article class="sheet">
    <div class="sheet-photo" role="img" aria-label="Photograph of ripe apricots filling the sheet background"></div>
    <section class="sheet-panel">
      <h1 class="sheet-title">APRICOT VARIETY SHEET</h1>
      <p class="sheet-origin">GROWN IN WASHINGTON STATE</p>
      <ul class="variety-list">
        <li class="variety">
          <h2 class="variety-name">RIVAL</h2>
          <p class="variety-text">Great flavor with a fine, firm texture distinguishes this large oval-shaped apricot. The skin is light orange<br>with a red blush. The flesh is a lush deep orange color. Available early July- early August.</p>
        </li>
        <li class="variety">
          <h2 class="variety-name">ROBADA</h2>
          <p class="variety-text">This jumbo apricot has a delicious floral flavor with a firm texture. Bright orange, with a deep red blush<br>over nearly half its surface. Available early June.</p>
        </li>
        <li class="variety">
          <h2 class="variety-name">PERFECTION</h2>
          <p class="variety-text">This classic large oval apricot is deep orange with an oblong shape and firm texture. The flesh is<br>a yellow/orange color that is very sweet and full of flavor. Available mid July - mid August.</p>
        </li>
        <li class="variety">
          <h2 class="variety-name">PATTERSON</h2>
          <p class="variety-text">This apricot has a well-balanced flavor and an excellent shelf life. This is perfect for canning or drying.<br>It has streaked red over yellow skin, with a firm flesh. Available mid – late June.</p>
        </li>
        <li class="variety">
          <h2 class="variety-name">TOMCOT</h2>
          <p class="variety-text">Tangy, sweet flavor with a firm texture. This oval apricot is light orange with a slight blush color.<br>The flesh is a dark orange. Available late June – late July.</p>
        </li>
        <li class="variety">
          <h2 class="variety-name">GOLDRICH</h2>
          <p class="variety-text">This apricot is round with a bright orange skin color and a deep orange flesh. It has a mild, sweet flavor<br>with a firm texture. Available early July – mid August.</p>
        </li>
        <li class="variety">
          <h2 class="variety-name">CASSELBRITE</h2>
          <p class="variety-text">This medium sized apricot is golden orange with a slight red blush. It has a mild sweet-tart flavor that<br>is good for eating out of hand. Available late June- early July.</p>
        </li>
        <li class="variety">
          <h2 class="variety-name">GOLDBAR</h2>
          <p class="variety-text">Moderately juicy, this large oval-shaped apricot has a light yellow-orange with a reddish blush.<br>The flesh is firm, meaty, and has a light orange color. Available late June – end of July.</p>
        </li>
        <li class="variety">
          <h2 class="variety-name">SWEET JUILLET</h2>
          <p class="variety-text">This special variety has a unique, sweet flavor with a juicy flesh. It is bright orange in color with a bright<br>orange flesh. Available through July.</p>
        </li>
        <li class="variety">
          <h2 class="variety-name">TASTY RICH</h2>
          <p class="variety-text">This early variety is light yellow-orange colored with a firm texture. Very juicy with an enticing flavor.<br>Available through June.</p>
        </li>
        <li class="variety">
          <h2 class="variety-name">GOLDSTRIKE</h2>
          <p class="variety-text">A larger apricot with light orange, blushed skin. Firm texture with a slight tart taste until fully ripened,<br>then very sweet. Available mid June - mid July.</p>
        </li>
        <li class="variety">
          <h2 class="variety-name">RILAND</h2>
          <p class="variety-text">Very aromatic and sweet, this apricot is orange with a red blush. It has a yellow-orange colored flesh and<br>a round shape. Available mid-June to end of July.</p>
        </li>
      </ul>
      <footer class="sheet-footer">www.meadowlarkorchard.com</footer>
    </section>
  </article>
</body>
</html>
```